Elegant, professional powerpoint design for Varomel Engineering and Mining SARLU

I’ve created a new Sub contracting company for mining industry in the Democratic Republic of Congo. With Quorvixel, I’ve created a logo. I would want a professional and beautiful powerpoint design which I will use to sell my services to mining companies in DRC. The powerpoint must have pictures of mining engines such as excavators, drones, trucks, etc

```html
<!DOCTYPE html>
<html lang="en">
<head>
<meta charset="utf-8">
<title>Varomel Engineering and Mining — Presentation Deck</title>
<link href="https://fonts.googleapis.com/css2?family=Oswald:wght@400;500&family=Open+Sans:wght@400;600&display=swap" rel="stylesheet">
<style>
:root{
  --navy:#1b1e6a;
  --navy-deep:#13155a;
  --gold:#f2a900;
  --gold-soft:#f6c24a;
  --ink:#2b2b3a;
  --muted:#8a8a95;
  --paper:#ffffff;
  --board:#c9c9cc;
  --light:#f1f1f3;
}
*{margin:0;padding:0;box-sizing:border-box}
html,body{width:1200px;height:1145px;overflow:hidden;background:var(--board)}
.deck{position:absolute;left:11px;top:13px;display:grid;grid-template-columns:repeat(5,226px);grid-auto-rows:127px;column-gap:12px;row-gap:14px}
.slide{position:relative;overflow:hidden;background:var(--paper);box-shadow:0 1px 3px rgba(0,0,0,.18)}
.a{position:absolute}
.navy{background:var(--navy)}
.gold{background:var(--gold)}
.light{background:var(--light)}
.title{font-family:'Oswald',sans-serif;font-weight:400;font-size:6.6px;line-height:1.15;color:var(--navy);text-transform:uppercase;letter-spacing:.1px}
.title.lg{font-size:9px}
.title.xl{font-size:13px}
.on-dark{color:#fff}
.accent{color:var(--gold)}
.label{font-family:'Oswald',sans-serif;font-size:3.3px;color:var(--navy);text-transform:uppercase;letter-spacing:.1px}
.copy{font-family:'Open Sans',sans-serif;font-size:2.4px;line-height:1.55;color:var(--muted)}
.copy.on-dark{color:#c9cbe6}
.num{font-family:'Oswald',sans-serif;font-size:6px;color:var(--gold)}
.stat{font-family:'Oswald',sans-serif;font-size:6px;color:#fff}
.brand{font-family:'Oswald',sans-serif;font-weight:500;font-size:4.4px;letter-spacing:.4px;color:var(--navy);display:flex;align-items:center;gap:2px}
.brand.on-dark{color:#fff}
.brand i{display:block;width:5px;height:5px;background:var(--gold)}
.photo-pit{background:linear-gradient(140deg,#8c7c66,#c8b798 45%,#6d6250)}
.photo-digger{background:linear-gradient(160deg,#cfd3d6,#e2c28a 45%,#d99a1e 65%,#5b4b36)}
.photo-dusk{background:linear-gradient(180deg,#e8b676,#c79255 50%,#5b4a39)}
.photo-worker{background:linear-gradient(180deg,#d7dbe0,#c7d04a 55%,#6f6a60)}
.photo-person{background:linear-gradient(180deg,#dcdfe3,#9aa2ad 60%,#3d434c)}
.photo-city{background:linear-gradient(180deg,#b9c5d3,#8c97a3 60%,#d9a435)}
.photo-dark{background:linear-gradient(160deg,#4b5058,#2d3138 60%,#5a5246)}
.photo-truck{background:linear-gradient(180deg,#b6c2cc,#d6b15b 55%,#7a6a52)}
.map{background:#d8d8dc}
.map-gold{background:linear-gradient(180deg,#d8d8dc 60%,var(--gold) 60%)}
.round{border-radius:50%}
.icon{width:9px;height:9px;border-radius:50%;background:var(--gold);display:flex;align-items:center;justify-content:center}
.icon svg{width:5px;height:5px}
.card{background:#fff;box-shadow:0 1px 2px rgba(0,0,0,.15)}
.bar{height:1.6px;background:#555}
.bar b{display:block;height:100%;background:var(--gold)}
.dot{width:7px;height:7px;border-radius:50%;background:var(--gold);font-family:'Oswald',sans-serif;font-size:2.4px;color:#fff;display:flex;align-items:center;justify-content:center}
</style>
</head>
<body>
<main class="deck">

<!-- 1 Cover -->
<section class="slide navy">
  <div class="a" style="left:0;top:0;width:226px;height:60px;background:#fff"></div>
  <div class="a photo-pit" role="img" aria-label="Aerial view of an open-pit mine" style="left:13px;top:13px;width:200px;height:47px"></div>
  <p class="a title on-dark" style="left:0;top:68px;width:226px;text-align:center">The presentation about</p>
  <p class="a title accent" style="left:0;top:76px;width:226px;text-align:center">Service mining company lorem of ipsum</p>
  <div class="a brand on-dark" style="left:96px;top:96px"><i></i>VAROMEL</div>
  <div class="a gold" style="left:0;top:124px;width:160px;height:3px"></div>
</section>

<!-- 2 Cover diagonal -->
<section class="slide">
  <div class="a photo-pit" role="img" aria-label="Bucket wheel excavator at a mine" style="left:0;top:0;width:226px;height:127px"></div>
  <svg class="a" style="left:0;top:0" width="226" height="127" viewBox="0 0 226 127">
    <polygon points="120,0 226,0 226,28 100,60" fill="#f2a900" opacity=".9"/>
    <polygon points="0,70 226,40 226,127 0,127" fill="#1b1e6a"/>
    <rect x="0" y="124" width="90" height="3" fill="#f2a900"/>
  </svg>
  <div class="a" style="left:98px;top:4px;width:30px"><div class="brand"><i></i>VAROMEL</div></div>
  <p class="a title on-dark" style="left:13px;top:93px;font-size:5px">The presentation about</p>
  <p class="a title accent" style="left:13px;top:100px">Service mining company<br>lorem of ipsum</p>
</section>

<!-- 3 Company profile -->
<section class="slide">
  <div class="a navy" style="left:0;top:0;width:14px;height:127px"></div>
  <p class="a label accent" style="left:27px;top:40px">Company profile</p>
  <p class="a title lg" style="left:27px;top:46px">Service mining<br>company</p>
  <p class="a copy" style="left:27px;top:70px;width:80px">Lorem ipsum dolor sit amet, consectetur adipiscing elit nam consequat ipsum accumsan facilisis.</p>
  <div class="a brand" style="left:27px;top:98px"><i></i>VAROMEL</div>
  <div class="a photo-worker" role="img" aria-label="Engineer in hard hat flying a survey drone" style="left:126px;top:13px;width:88px;height:95px"></div>
  <div class="a gold" style="left:200px;top:13px;width:14px;height:14px;clip-path:polygon(0 0,100% 0,100% 100%)"></div>
</section>

<!-- 4 Intro with author -->
<section class="slide">
  <div class="a photo-pit" role="img" aria-label="Terraced open-pit mine from above" style="left:110px;top:0;width:116px;height:127px"></div>
  <svg class="a" style="left:0;top:0" width="140" height="127"><polygon points="0,0 122,0 108,127 0,127" fill="#1b1e6a"/></svg>
  <p class="a title on-dark" style="left:14px;top:22px">Service mining company<br>lorem of ipsum</p>
  <p class="a copy on-dark" style="left:14px;top:40px;width:85px">Phasellus vitae ipsum non enim bibendum porttitor sed a pulvinar arcu. Lorem dapibus risus id quam metus proin vestibulum, mi vel tempor tempor.</p>
  <p class="a copy on-dark" style="left:14px;top:62px;width:85px">Aliquam lacus elit, condimentum sit amet mauris eu, molestie elementum lorem. Praesent pulvinar turpis sed dolor congue.</p>
  <div class="a photo-person round" role="img" aria-label="Portrait of the site builder" style="left:14px;top:95px;width:12px;height:12px"></div>
  <p class="a label on-dark" style="left:30px;top:97px">Marcus Hale</p>
  <p class="a copy accent" style="left:30px;top:102px">Main Builder</p>
</section>

<!-- 5 Explore -->
<section class="slide">
  <div class="a navy" style="left:0;top:0;width:93px;height:127px"></div>
  <div class="a brand on-dark" style="left:34px;top:14px"><i></i>VAROMEL</div>
  <p class="a title on-dark lg" style="left:0;top:44px;width:93px;text-align:center">Explore our<br>world of<br>mining</p>
  <div class="a gold" style="left:14px;top:112px;width:54px;height:1.5px"></div>
  <p class="a copy" style="left:108px;top:28px;width:105px;color:var(--ink);font-size:2.8px">Proin quis ornare dolor curabitur nulla magna, blandit at pharetra ut porttitor sed libero nunc sagittis mi non cursus.</p>
  <p class="a copy" style="left:108px;top:46px;width:105px">Duis sodales aliquet nibh eget porta dapibus volutpat enim at lobortis suspendisse potenti fusce eu purus augue lorem ipsum dolor sit amet.</p>
  <p class="a copy" style="left:108px;top:63px;width:105px">Porttitor sed cursus ut sit amet lectus volutpat vel consectetur sollicitudin nullam in venenatis lectus quis tortor.</p>
  <p class="a copy" style="left:108px;top:80px;width:105px">Sed ultricies faucibus rhoncus aliquam consequat faucibus massa sed maximus dui feugiat donec in nulla erat.</p>
</section>

<!-- 6 About us -->
<section class="slide">
  <div class="a photo-dusk" role="img" aria-label="Excavator working at a quarry" style="left:14px;top:0;width:96px;height:44px"></div>
  <div class="a navy" style="left:110px;top:0;width:116px;height:44px"></div>
  <div class="a gold" style="left:110px;top:44px;width:116px;height:13px"></div>
  <p class="a label on-dark" style="left:132px;top:14px">Our mission</p>
  <p class="a copy on-dark" style="left:132px;top:20px;width:80px">Aliquam mattis aliquam imperdiet sed suscipit varius orci id mollis enim vulputate convallis erat et rhoncus.</p>
  <p class="a title" style="left:15px;top:73px;color:var(--navy)">About us</p>
  <div class="a gold" style="left:15px;top:82px;width:26px;height:1px"></div>
  <p class="a copy" style="left:15px;top:87px;width:90px">Lorem ipsum dolor sit amet, consectetur adipiscing elit nam consequat id ipsum accumsan facilisis ligula lorem hendrerit nec libero.</p>
  <p class="a copy" style="left:15px;top:103px;width:90px">Maecenas convallis erat et rhoncus scelerisque lorem non leo dictum.</p>
  <p class="a label" style="left:132px;top:72px">Our vision</p>
  <p class="a copy" style="left:132px;top:78px;width:80px">Aliquam mattis aliquam imperdiet sed suscipit varius orci id mollis enim vulputate.</p>
  <p class="a label" style="left:132px;top:96px">Our goals</p>
  <p class="a copy" style="left:132px;top:102px;width:80px">Aliquam mattis aliquam imperdiet sed suscipit varius orci id mollis enim vulputate.</p>
</section>

<!-- 7 Why choose us -->
<section class="slide">
  <p class="a title" style="left:15px;top:14px">Why choose us?</p>
  <div class="a gold" style="left:15px;top:23px;width:26px;height:1px"></div>
  <p class="a copy" style="left:15px;top:30px;width:60px">Lorem ipsum dolor sit amet consectetur adipiscing elit nam consequat et ipsum accumsan donec.</p>
  <p class="a copy" style="left:15px;top:45px;width:60px">Phasellus accumsan nunc id tempus accumsan, urna dolor sollicitudin tellus, eu rutrum justo.</p>
  <div class="a photo-dusk" role="img" aria-label="Two excavators at sunset" style="left:82px;top:0;width:144px;height:72px"></div>
  <div class="a navy" style="left:0;top:72px;width:226px;height:55px"></div>
  <p class="a label accent" style="left:15px;top:86px">Advantages</p>
  <p class="a copy on-dark" style="left:15px;top:93px;width:60px">Sed id eros eu massa viverra sagittis id nec metus enim justo malesuada.</p>
  <p class="a copy on-dark" style="left:88px;top:93px;width:55px">• Pellentesque in lectus lacinia, eleifend felis eu.<br>• Curabitur nec est quis dui placerat.</p>
  <p class="a stat" style="left:172px;top:100px">10 000</p>
  <p class="a copy on-dark" style="left:166px;top:110px">Customers have already trusted us</p>
</section>

<!-- 8 Builder company -->
<section class="slide">
  <p class="a title" style="left:14px;top:15px">About our<br>builder company</p>
  <p class="a copy" style="left:14px;top:36px;width:92px">Lorem ipsum dolor sit amet, consectetur adipiscing elit nam consequat id ipsum accumsan facilisis ligula lorem hendrerit nec libero aliquet mattis aliquam.</p>
  <div class="a" style="left:14px;top:61px;width:92px;height:.5px;background:#ddd"></div>
  <div class="a navy" style="left:14px;top:72px;width:42px;height:37px"></div>
  <p class="a stat" style="left:20px;top:80px">+35 285</p>
  <p class="a copy on-dark" style="left:18px;top:92px;width:34px;text-align:center">Duis consectetur lacus sed neque</p>
  <div class="a gold" style="left:63px;top:72px;width:42px;height:37px"></div>
  <p class="a stat" style="left:72px;top:80px">93.3%</p>
  <p class="a copy on-dark" style="left:67px;top:92px;width:34px;text-align:center">Duis consectetur lacus sed neque</p>
  <div class="a photo-truck" role="img" aria-label="Wheel loader at a sand pit" style="left:120px;top:14px;width:92px;height:82px"></div>
  <div class="a navy" style="left:0;top:124px;width:226px;height:3px"></div>
</section>

<!-- 9 Professional team -->
<section class="slide">
  <div class="a photo-worker" role="img" aria-label="Engineer in safety vest with tablet" style="left:0;top:0;width:47px;height:127px"></div>
  <p class="a title lg" style="left:62px;top:36px">We are a<br>professional<br>team of <span class="accent">mining<br>services</span></p>
  <div class="a gold" style="left:135px;top:0;width:91px;height:127px"></div>
  <p class="a label on-dark" style="left:150px;top:29px"><span style="font-size:5px">01.</span> Qualified staff</p>
  <p class="a copy on-dark" style="left:150px;top:38px;width:62px">Proin et dui eleifend, consectetur tortor eu, pulvinar enim.</p>
  <p class="a label on-dark" style="left:150px;top:55px"><span style="font-size:5px">02.</span> The best building materials</p>
  <p class="a copy on-dark" style="left:150px;top:64px;width:62px">Quisque in sapien commodo nunc hendrerit sodales.</p>
  <p class="a label on-dark" style="left:150px;top:81px"><span style="font-size:5px">03.</span> Realization on time</p>
  <p class="a copy on-dark" style="left:150px;top:90px;width:62px">Aliquam varius laoreet turpis et consectetur amet nisl.</p>
</section>

<!-- 10 Mining company -->
<section class="slide">
  <div class="a photo-pit" role="img" aria-label="Haul truck in an open-pit mine" style="left:0;top:0;width:100px;height:127px"></div>
  <svg class="a" style="left:94px;top:0" width="16" height="127"><polygon points="4,0 16,0 16,127 0,127" fill="#fff"/><line x1="6" y1="0" x2="2" y2="127" stroke="#f2a900" stroke-width="1.5"/></svg>
  <p class="a title" style="left:134px;top:23px">Mining company<br><span class="accent">and lorem business</span></p>
  <p class="a copy" style="left:134px;top:42px;width:80px">Lorem ipsum dolor sit amet consectetur adipiscing elit nam consequat ipsum accumsan.</p>
  <svg class="a" style="left:134px;top:66px" width="6" height="6"><circle cx="3" cy="3" r="2.5" fill="none" stroke="#1b1e6a" stroke-width=".6"/><path d="M1.7 3l1 1 1.6-1.8" fill="none" stroke="#1b1e6a" stroke-width=".6"/></svg>
  <p class="a label" style="left:143px;top:66px">Building an economic system</p>
  <p class="a copy" style="left:143px;top:72px;width:72px">Aenean sodales vestibulum lobortis sed convallis semper odio.</p>
  <svg class="a" style="left:134px;top:90px" width="6" height="6"><circle cx="3" cy="3" r="2.5" fill="none" stroke="#1b1e6a" stroke-width=".6"/><path d="M1.7 3l1 1 1.6-1.8" fill="none" stroke="#1b1e6a" stroke-width=".6"/></svg>
  <p class="a label" style="left:143px;top:90px">Prefabricated houses</p>
  <p class="a copy" style="left:143px;top:96px;width:72px">Praesent vel metus lacinia purus id amet malesuada.</p>
</section>

<!-- 11 Get to know -->
<section class="slide">
  <p class="a title" style="left:15px;top:22px">Get to know<br>our company closer</p>
  <p class="a copy" style="left:15px;top:42px;width:90px">Lorem ipsum dolor sit amet consectetur adipiscing elit nam consequat id ipsum accumsan facilisis ligula lorem.</p>
  <p class="a copy" style="left:15px;top:58px;width:90px">Mauris faucibus nunc aliquet vehicula aliquet felis mi volutpat id blandit dolor sodales.</p>
  <svg class="a" style="left:16px;top:84px" width="10" height="12"><circle cx="5" cy="5" r="3" fill="none" stroke="#f2a900" stroke-width=".7"/><rect x="3.8" y="8.5" width="2.4" height="2" fill="#f2a900"/></svg>
  <p class="a label" style="left:30px;top:84px">The main idea of our company</p>
  <p class="a copy" style="left:30px;top:90px;width:65px">Integer volutpat auctor nisi vulputate vitae ullamcorper.</p>
  <div class="a navy" style="left:0;top:124px;width:94px;height:3px"></div>
  <div class="a photo-pit" role="img" aria-label="Architectural site with construction cranes" style="left:132px;top:0;width:94px;height:127px"></div>
  <div class="a card" style="left:120px;top:13px;width:80px;height:27px"></div>
  <div class="a card" style="left:120px;top:48px;width:80px;height:27px"></div>
  <div class="a card" style="left:120px;top:83px;width:80px;height:27px"></div>
  <p class="a num" style="left:126px;top:20px">01.</p><p class="a label" style="left:140px;top:20px">Architectural design</p>
  <p class="a copy" style="left:140px;top:26px;width:55px">Proin in nisi eleifend, consectetur tortor donec pulvinar.</p>
  <p class="a num" style="left:126px;top:55px">02.</p><p class="a label" style="left:140px;top:55px">Construction works</p>
  <p class="a copy" style="left:140px;top:61px;width:55px">Sed eu eleifend mi, condimentum urna mollis tempor.</p>
  <p class="a num" style="left:126px;top:90px">03.</p><p class="a label" style="left:140px;top:90px">Interior finishing</p>
  <p class="a copy" style="left:140px;top:96px;width:55px">Etiam augue mi, tincidunt vitae mi scelerisque.</p>
</section>

<!-- 12 Creative company -->
<section class="slide">
  <div class="a navy" style="left:0;top:0;width:60px;height:127px"></div>
  <p class="a stat accent" style="left:22px;top:20px">25 823</p>
  <p class="a copy on-dark" style="left:14px;top:30px;width:34px;text-align:center">Satisfied customers with the services</p>
  <p class="a stat accent" style="left:22px;top:54px">18 359</p>
  <p class="a copy on-dark" style="left:14px;top:64px;width:34px;text-align:center">Built apartments for developers</p>
  <p class="a stat accent" style="left:21px;top:88px">356 982</p>
  <p class="a copy on-dark" style="left:14px;top:98px;width:34px;text-align:center">Used tons of concrete for construction</p>
  <div class="a photo-digger" role="img" aria-label="Yellow backhoe loader on site" style="left:60px;top:0;width:60px;height:127px"></div>
  <p class="a title" style="left:134px;top:22px"><span class="accent">A creative</span><br>lorem ipsum company</p>
  <p class="a copy" style="left:134px;top:42px;width:80px">Phasellus rhoncus leo in viverra cursus commodo aliquam laoreet aliquam neque et tortor dapibus volutpat.</p>
  <p class="a copy" style="left:134px;top:60px;width:80px">Donec aliquet nibh mattis nulla elementum eget rhoncus leo suscipit id.</p>
  <p class="a copy" style="left:134px;top:74px;width:80px">Mauris nunc sapien, condimentum ac sapien vitae pretium mauris nibh metus.</p>
  <div class="a" style="left:134px;top:90px;width:80px;height:.5px;background:#ddd"></div>
  <p class="a label" style="left:134px;top:98px">Marcus Hale</p>
  <p class="a copy accent" style="left:134px;top:103px">Main Builder</p>
</section>

<!-- 13 Experts -->
<section class="slide">
  <p class="a title" style="left:15px;top:14px">Meet our experts</p>
  <p class="a copy" style="left:84px;top:14px;width:130px">Morbi aliquam vestibulum tellus dictum ligula non dolor mollis, quis pretium turpis bibendum facilisis fringilla sapien et commodo semper.</p>
  <div class="a navy" style="left:0;top:70px;width:226px;height:57px"></div>
  <div class="a photo-person round" role="img" aria-label="Portrait of the main architect" style="left:14px;top:40px;width:44px;height:44px"></div>
  <div class="a photo-person round" role="img" aria-label="Portrait of the main builder" style="left:65px;top:40px;width:44px;height:44px"></div>
  <div class="a photo-worker round" role="img" aria-label="Portrait of the site foreman" style="left:116px;top:40px;width:44px;height:44px"></div>
  <div class="a photo-person round" role="img" aria-label="Portrait of a builder" style="left:167px;top:40px;width:44px;height:44px"></div>
  <p class="a label on-dark" style="left:14px;top:92px;width:44px;text-align:center">Elena Voss<br><span class="accent">Main Architect</span></p>
  <p class="a label on-dark" style="left:65px;top:92px;width:44px;text-align:center">Marcus Hale<br><span class="accent">Main Builder</span></p>
  <p class="a label on-dark" style="left:116px;top:92px;width:44px;text-align:center">Owen Pratt<br><span class="accent">Foreman</span></p>
  <p class="a label on-dark" style="left:167px;top:92px;width:44px;text-align:center">Leo Brandt<br><span class="accent">Builder</span></p>
  <p class="a copy on-dark" style="left:14px;top:104px;width:44px;text-align:center">E. elena@varomel.com<br>T. +44 1204 390281</p>
  <p class="a copy on-dark" style="left:65px;top:104px;width:44px;text-align:center">E. marcus@varomel.com<br>T. +44 1204 390282</p>
  <p class="a copy on-dark" style="left:116px;top:104px;width:44px;text-align:center">E. owen@varomel.com<br>T. +44 1204 390283</p>
  <p class="a copy on-dark" style="left:167px;top:104px;width:44px;text-align:center">E. leo@varomel.com<br>T. +44 1204 390284</p>
</section>

<!-- 14 Profile with skills -->
<section class="slide">
  <div class="a photo-person round" role="img" aria-label="Portrait of the main builder" style="left:14px;top:20px;width:84px;height:84px"></div>
  <p class="a title" style="left:128px;top:26px">Marcus Hale</p>
  <p class="a copy accent" style="left:128px;top:35px">Main Builder</p>
  <p class="a copy" style="left:128px;top:45px;width:84px">Cras sed rutrum id nec vivamus laoreet luctus imperdiet dictum magna lacus nec quisque vulputate.</p>
  <p class="a copy" style="left:128px;top:60px;width:84px">Suspendisse sit amet lectus massa convallis et turpis eu semper.</p>
  <p class="a copy" style="left:128px;top:78px">Architecture</p><div class="a bar" style="left:145px;top:79px;width:68px"><b style="width:82%"></b></div>
  <p class="a copy" style="left:128px;top:84px">Build</p><div class="a bar" style="left:145px;top:85px;width:68px"><b style="width:70%"></b></div>
  <p class="a copy" style="left:128px;top:90px">Constructor</p><div class="a bar" style="left:145px;top:91px;width:68px"><b style="width:76%"></b></div>
  <p class="a copy" style="left:128px;top:96px">Planning</p><div class="a bar" style="left:145px;top:97px;width:68px"><b style="width:64%"></b></div>
</section>

<!-- 15 Architect profile -->
<section class="slide light">
  <div class="a navy" style="left:0;top:0;width:100px;height:127px"></div>
  <div class="a" style="left:14px;top:13px;width:100px;height:100px;background:#fff;border-radius:8px"></div>
  <div class="a photo-worker round" role="img" aria-label="Portrait of the main architect in hard hat" style="left:30px;top:29px;width:68px;height:68px"></div>
  <p class="a title xl" style="left:128px;top:16px">Elena<br><span class="accent">Voss</span></p>
  <p class="a label" style="left:128px;top:62px">Main architect</p>
  <p class="a copy" style="left:128px;top:68px;width:40px">Duis sollicitudin sollicitudin nibh sed molestie nisl aliquet dapibus maecenas a urna.</p>
  <p class="a label" style="left:181px;top:62px">Experience</p>
  <p class="a copy" style="left:181px;top:68px;width:34px">Aenean blandit rhoncus enim id amet nisi vestibulum tellus.</p>
  <p class="a copy" style="left:128px;top:95px;width:80px">Donec ipsum eu velit, consectetur id amet pellentesque donec dapibus a varius.</p>
</section>

<!-- 16 History -->
<section class="slide">
  <p class="a title" style="left:15px;top:15px">The history<br>of our company</p>
  <p class="a copy" style="left:15px;top:34px;width:92px">Lorem ipsum dolor sit amet consectetur adipiscing elit mauris volutpat augue euismod augue nec venenatis.</p>
  <div class="a photo-worker" role="img" aria-label="Hands operating a drone remote controller" style="left:0;top:58px;width:107px;height:40px"></div>
  <p class="a copy" style="left:15px;top:106px;width:92px">Lorem ipsum dolor sit amet consectetur adipiscing elit nam consequat id ipsum accumsan.</p>
  <div class="a" style="left:126px;top:10px;width:.5px;height:117px;background:#e0c27a"></div>
  <div class="a dot" style="left:122.5px;top:15px">1982</div>
  <div class="a dot" style="left:122.5px;top:43px">1998</div>
  <div class="a dot" style="left:122.5px;top:71px">2006</div>
  <div class="a dot" style="left:122.5px;top:99px">2012</div>
  <p class="a label" style="left:138px;top:15px">Starting a business</p><p class="a copy" style="left:138px;top:21px;width:76px">Cras aliquam, justo eget efficitur pretium, risus ipsum hendrerit arcu.</p>
  <p class="a label" style="left:138px;top:43px">Business development</p><p class="a copy" style="left:138px;top:49px;width:76px">Sed rhoncus tortor sit amet ligula porttitor in lobortis dolor fringilla.</p>
  <p class="a label" style="left:138px;top:71px">New work places</p><p class="a copy" style="left:138px;top:77px;width:76px">Orci varius natoque penatibus et magnis dis parturient montes.</p>
  <p class="a label" style="left:138px;top:99px">Cooperation with Norvale</p><p class="a copy" style="left:138px;top:105px;width:76px">Suspendisse at ornare est sed tortor volutpat id tempor luctus.</p>
</section>

<!-- 17 Story -->
<section class="slide">
  <p class="a label" style="left:15px;top:17px">Get to know our story to<br>the end and see for yourself</p>
  <p class="a copy" style="left:15px;top:30px;width:90px">Duis ut enim interdum hendrerit finibus aenean auctor mi vel commodo ultricies nibh eros metus.</p>
  <p class="a copy" style="left:15px;top:46px;width:90px">Etiam ipsum gravida lorem tristique tempus sapien vel magna vitae commodo.</p>
  <div class="a photo-city" role="img" aria-label="Industrial drone on a white floor" style="left:15px;top:70px;width:41px;height:30px"></div>
  <div class="a photo-digger" role="img" aria-label="Yellow loader at a residential site" style="left:63px;top:70px;width:41px;height:30px"></div>
  <p class="a copy" style="left:15px;top:103px;width:41px;text-align:center">Advanced construction machine</p>
  <p class="a copy" style="left:63px;top:103px;width:41px;text-align:center">Residential apartments for sale</p>
  <div class="a gold" style="left:15px;top:112px;width:41px;height:1px"></div>
  <div class="a gold" style="left:63px;top:112px;width:41px;height:1px"></div>
  <div class="a" style="left:126px;top:10px;width:.5px;height:117px;background:#e0c27a"></div>
  <div class="a dot" style="left:122.5px;top:15px">2013</div>
  <div class="a dot" style="left:122.5px;top:43px">2017</div>
  <div class="a dot" style="left:122.5px;top:71px">2019</div>
  <div class="a dot navy" style="left:120.5px;top:97px;width:11px;height:11px">2021</div>
  <p class="a label" style="left:138px;top:15px">Construction of a birch estate</p><p class="a copy" style="left:138px;top:21px;width:76px">Proin ultricies porttitor massa eu placerat aenean ac rutrum orci.</p>
  <p class="a label" style="left:138px;top:43px">Construction of apartments</p><p class="a copy" style="left:138px;top:49px;width:76px">Phasellus eros purus tincidunt ut ipsum vel dignissim tempor.</p>
  <p class="a label" style="left:138px;top:71px">Investment in machine development</p><p class="a copy" style="left:138px;top:77px;width:76px">Integer efficitur leo a venenatis imperdiet lacus nulla.</p>
  <p class="a label" style="left:138px;top:99px">Win the builder award</p><p class="a copy" style="left:138px;top:105px;width:76px">Morbi bibendum metus quis faucibus fringilla cras quis mattis.</p>
</section>

<!-- 18 Services with side photo -->
<section class="slide">
  <div class="a photo-dusk" role="img" aria-label="Excavator at a river construction site" style="left:0;top:0;width:40px;height:127px"></div>
  <div class="a card" style="left:40px;top:13px;width:64px;height:100px;box-shadow:none"></div>
  <p class="a title" style="left:55px;top:39px">Our services</p>
  <p class="a copy" style="left:55px;top:50px;width:45px">Proin quis ornare dolor curabitur nulla magna blandit at pharetra ut porttitor sed libero nunc sagittis.</p>
  <p class="a copy" style="left:55px;top:72px;width:45px">Nulla vel sagittis justo phasellus vehicula elit ut sed nulla.</p>
  <div class="a icon" style="left:120px;top:26px;width:12px;height:12px"><svg viewBox="0 0 10 10"><path d="M1 5L5 1l4 4v4H1z" fill="none" stroke="#fff"/></svg></div>
  <p class="a label" style="left:140px;top:26px">House building</p><p class="a copy" style="left:140px;top:32px;width:74px">Nam sit amet libero at mi elementum vulputate non in gravida.</p>
  <div class="a icon" style="left:120px;top:54px;width:12px;height:12px"><svg viewBox="0 0 10 10"><rect x="1" y="3" width="8" height="5" fill="none" stroke="#fff"/></svg></div>
  <p class="a label" style="left:140px;top:54px">Concrete surfaces</p><p class="a copy" style="left:140px;top:60px;width:74px">Duis tempus lectus in ultricies elementum ligula ex fermentum.</p>
  <div class="a icon" style="left:120px;top:82px;width:12px;height:12px"><svg viewBox="0 0 10 10"><path d="M2 8l6-6M2 2l6 6" stroke="#fff"/></svg></div>
  <p class="a label" style="left:140px;top:82px">Renovation</p><p class="a copy" style="left:140px;top:88px;width:74px">Sed convallis nunc eu nisl venenatis nec sagittis augue sagittis.</p>
</section>

<!-- 19 Team offers -->
<section class="slide">
  <p class="a title" style="left:15px;top:15px">Our team offers<br>services</p>
  <p class="a copy" style="left:15px;top:34px;width:75px">Lorem ipsum dolor sit amet consectetur adipiscing elit nam consequat et ipsum accumsan facilisis ligula lorem.</p>
  <div class="a photo-pit" role="img" aria-label="Open-pit mine landscape" style="left:82px;top:0;width:134px;height:62px"></div>
  <div class="a gold" style="left:216px;top:0;width:10px;height:12px"></div>
  <p class="a label" style="left:15px;top:70px"><span class="num" style="font-size:5px">01.</span> Designing &amp; construction</p>
  <p class="a label" style="left:83px;top:70px"><span class="num" style="font-size:5px">02.</span> Steel &amp; concrete building</p>
  <p class="a label" style="left:151px;top:70px"><span class="num" style="font-size:5px">03.</span> Professional team</p>
  <p class="a copy" style="left:15px;top:79px;width:60px">Donec massa ante maximus condimentum tortor imperdiet.</p>
  <p class="a copy" style="left:83px;top:79px;width:60px">Donec massa ante maximus condimentum tortor imperdiet.</p>
  <p class="a copy" style="left:151px;top:79px;width:60px">Donec massa ante maximus condimentum tortor imperdiet.</p>
  <p class="a label" style="left:15px;top:96px"><span class="num" style="font-size:5px">04.</span> Interior finish</p>
  <p class="a label" style="left:83px;top:96px"><span class="num" style="font-size:5px">05.</span> High-quality materials</p>
  <p class="a label" style="left:151px;top:96px"><span class="num" style="font-size:5px">06.</span> Support on site</p>
  <p class="a copy" style="left:15px;top:105px;width:60px">Donec massa ante maximus condimentum tortor imperdiet.</p>
  <p class="a copy" style="left:83px;top:105px;width:60px">Donec massa ante maximus condimentum tortor imperdiet.</p>
  <p class="a copy" style="left:151px;top:105px;width:60px">Donec massa ante maximus condimentum tortor imperdiet.</p>
</section>

<!-- 20 Services top photo -->
<section class="slide">
  <div class="a photo-truck" role="img" aria-label="Haul truck at an open-pit mine" style="left:29px;top:0;width:197px;height:80px"></div>
  <div class="a card" style="left:14px;top:16px;width:72px;height:48px;box-shadow:none"></div>
  <p class="a title" style="left:22px;top:28px">Our services</p>
  <p class="a copy" style="left:22px;top:40px;width:58px">Proin quis ornare dolor curabitur nulla magna blandit at pharetra ut porttitor sed.</p>
  <div class="a icon navy" style="left:16px;top:94px;width:13px;height:13px"><svg viewBox="0 0 10 10"><path d="M1 5L5 1l4 4v4H1z" fill="none" stroke="#fff"/></svg></div>
  <p class="a label" style="left:33px;top:93px">House building</p><p class="a copy" style="left:33px;top:99px;width:38px">Nam sit amet libero at mi elementum vulputate.</p>
  <div class="a icon" style="left:84px;top:94px;width:13px;height:13px"><svg viewBox="0 0 10 10"><rect x="1" y="3" width="8" height="5" fill="none" stroke="#fff"/></svg></div>
  <p class="a label" style="left:101px;top:93px">Concrete surfaces</p><p class="a copy" style="left:101px;top:99px;width:38px">Duis tempus lectus in ultricies elementum ligula.</p>
  <div class="a icon" style="left:152px;top:94px;width:13px;height:13px"><svg viewBox="0 0 10 10"><path d="M2 8l6-6M2 2l6 6" stroke="#fff"/></svg></div>
  <p class="a label" style="left:169px;top:93px">Renovation</p><p class="a copy" style="left:169px;top:99px;width:45px">Sed convallis nunc eu nisl venenatis nec sagittis.</p>
</section>

<!-- 21 Services quadrants -->
<section class="slide">
  <p class="a title" style="left:12px;top:20px">Our services</p>
  <div class="a gold" style="left:12px;top:29px;width:22px;height:1px"></div>
  <p class="a copy" style="left:12px;top:34px;width:60px">Proin quis ornare dolor curabitur nulla magna blandit at pharetra ut porttitor sed libero nunc sagittis.</p>
  <div class="a gold" style="left:75px;top:0;width:151px;height:63px"></div>
  <div class="a" style="left:150px;top:0;width:.5px;height:63px;background:#f7d27a"></div>
  <svg class="a" style="left:84px;top:22px" width="9" height="9"><path d="M1 5L4.5 1.5 8 5v3H1z" fill="none" stroke="#fff" stroke-width=".7"/></svg>
  <p class="a label on-dark" style="left:96px;top:21px">House building</p>
  <p class="a copy on-dark" style="left:96px;top:27px;width:48px">Nam sit amet libero at mi elementum vulputate non in gravida lorem.</p>
  <svg class="a" style="left:159px;top:22px" width="9" height="9"><rect x="1" y="3" width="7" height="4" fill="none" stroke="#fff" stroke-width=".7"/></svg>
  <p class="a label on-dark" style="left:171px;top:21px">Concrete surfaces</p>
  <p class="a copy on-dark" style="left:171px;top:27px;width:48px">Duis consectetur leo vel neque feugiat nec vehicula sem et.</p>
  <div class="a photo-dusk" role="img" aria-label="Excavator on a levelled construction site" style="left:0;top:63px;width:150px;height:64px"></div>
  <div class="a navy" style="left:150px;top:63px;width:76px;height:64px"></div>
  <svg class="a" style="left:159px;top:85px" width="9" height="9"><path d="M2 7l5-5M2 2l5 5" stroke="#fff" stroke-width=".7"/></svg>
  <p class="a label on-dark" style="left:171px;top:84px">Renovation</p>
  <p class="a copy on-dark" style="left:171px;top:90px;width:48px">Integer eget mi faucibus porta magna sed molestie nisi.</p>
</section>

<!-- 22 Services cards -->
<section class="slide">
  <p class="a title" style="left:0;top:15px;width:226px;text-align:center">Our services</p>
  <p class="a copy" style="left:38px;top:29px;width:150px;text-align:center">Praesent nulla libero, luctus ac est eu, hendrerit molestie odio nunc quis ante dignissim nulla tincidunt pulvinar ante felis mollis nec viverra.</p>
  <div class="a navy" style="left:0;top:67px;width:226px;height:60px"></div>
  <div class="a card" style="left:14px;top:52px;width:46px;height:59px"></div>
  <div class="a card" style="left:64px;top:52px;width:46px;height:59px"></div>
  <div class="a card" style="left:116px;top:52px;width:46px;height:59px"></div>
  <div class="a card" style="left:166px;top:52px;width:46px;height:59px"></div>
  <p class="a label" style="left:14px;top:78px;width:46px;text-align:center">House building</p>
  <p class="a label" style="left:64px;top:78px;width:46px;text-align:center">Concrete surfaces</p>
  <p class="a label" style="left:116px;top:78px;width:46px;text-align:center">Drilling wallies</p>
  <p class="a label" style="left:166px;top:78px;width:46px;text-align:center">Renovation</p>
  <p class="a copy" style="left:17px;top:84px;width:40px;text-align:center">Nam sit amet libero at mi donec vulputate.</p>
  <p class="a copy" style="left:67px;top:84px;width:40px;text-align:center">Donec luctus leo eu auctor amet luctus.</p>
  <p class="a copy" style="left:119px;top:84px;width:40px;text-align:center">Suspendisse facilisis venenatis dolor non.</p>
  <p class="a copy" style="left:169px;top:84px;width:40px;text-align:center">Fusce vitae laoreet felis dapibus placerat.</p>
  <div class="a icon" style="left:33px;top:64px;background:none"><svg viewBox="0 0 10 10"><path d="M1 5L5 1l4 4v4H1z" fill="none" stroke="#f2a900"/></svg></div>
  <div class="a icon" style="left:83px;top:64px;background:none"><svg viewBox="0 0 10 10"><rect x="1" y="3" width="8" height="5" fill="none" stroke="#f2a900"/></svg></div>
  <div class="a icon" style="left:135px;top:64px;background:none"><svg viewBox="0 0 10 10"><path d="M1 4h6v3H1z" fill="none" stroke="#f2a900"/></svg></div>
  <div class="a icon" style="left:185px;top:64px;background:none"><svg viewBox="0 0 10 10"><path d="M2 8l6-6M2 2l6 6" stroke="#f2a900"/></svg></div>
</section>

<!-- 23 Architectural services -->
<section class="slide">
  <p class="a title" style="left:15px;top:25px">Architectural services</p>
  <svg class="a" style="left:15px;top:47px" width="8" height="8"><path d="M1 4.5L4 1.5 7 4.5V7H1z" fill="none" stroke="#f2a900" stroke-width=".7"/></svg>
  <p class="a label" style="left:27px;top:48px">House building</p><p class="a copy" style="left:27px;top:54px;width:40px">Sed feugiat blandit tincidunt sit luctus fringilla.</p>
  <svg class="a" style="left:83px;top:47px" width="8" height="8"><rect x="1" y="2" width="6" height="4" fill="none" stroke="#f2a900" stroke-width=".7"/></svg>
  <p class="a label" style="left:95px;top:48px">Concrete surfaces</p><p class="a copy" style="left:95px;top:54px;width:40px">Nam sit est ultrices lacinia integer tempor.</p>
  <svg class="a" style="left:15px;top:80px" width="8" height="8"><path d="M1 3h5v3H1z" fill="none" stroke="#f2a900" stroke-width=".7"/></svg>
  <p class="a label" style="left:27px;top:81px">Drilling wallies</p><p class="a copy" style="left:27px;top:87px;width:40px">Nam pulvinar sit vel congue fusce amet iaculis.</p>
  <svg class="a" style="left:83px;top:80px" width="8" height="8"><path d="M1 7l6-6M1 1l6 6" stroke="#f2a900" stroke-width=".7"/></svg>
  <p class="a label" style="left:95px;top:81px">Renovation</p><p class="a copy" style="left:95px;top:87px;width:40px">Quisque in sapien commodo tellus tristique.</p>
  <div class="a navy" style="left:170px;top:0;width:56px;height:15px"></div>
  <div class="a photo-dusk" role="img" aria-label="Yellow excavator under a sunset sky" style="left:154px;top:15px;width:72px;height:112px"></div>
</section>

<!-- 24 Architectural and construction -->
<section class="slide">
  <div class="a navy" style="left:14px;top:13px;width:198px;height:45px"></div>
  <p class="a title on-dark" style="left:28px;top:23px">Architectural<br>and construction<br>services</p>
  <div class="a gold" style="left:28px;top:47px;width:22px;height:1px"></div>
  <p class="a copy on-dark" style="left:108px;top:24px;width:90px">Praesent nulla libero luctus ac est eu hendrerit molestie odio nunc quis ante dignissim nulla tincidunt pulvinar.</p>
  <svg class="a" style="left:14px;top:75px" width="9" height="9"><path d="M1 5L4.5 1.5 8 5v3H1z" fill="none" stroke="#f2a900" stroke-width=".7"/></svg>
  <p class="a label" style="left:27px;top:75px">House building</p><p class="a copy" style="left:27px;top:81px;width:44px">Sed feugiat blandit tincidunt sit et luctus fringilla.</p>
  <svg class="a" style="left:82px;top:75px" width="9" height="9"><path d="M1 3h6v3H1z" fill="none" stroke="#f2a900" stroke-width=".7"/></svg>
  <p class="a label" style="left:95px;top:75px">Drilling wallies</p><p class="a copy" style="left:95px;top:81px;width:44px">Nam pulvinar sit vel congue fusce amet iaculis.</p>
  <svg class="a" style="left:150px;top:75px" width="9" height="9"><path d="M1 8l7-7M1 1l7 7" stroke="#f2a900" stroke-width=".7"/></svg>
  <p class="a label" style="left:163px;top:75px">Renovation</p><p class="a copy" style="left:163px;top:81px;width:48px">Quisque in sapien commodo tellus tristique.</p>
</section>

<!-- 25 Mining company services -->
<section class="slide">
  <div class="a photo-pit" role="img" aria-label="Loader filling a truck at a mine" style="left:0;top:0;width:120px;height:75px"></div>
  <div class="a navy" style="left:214px;top:3px;width:10px;height:10px"></div>
  <p class="a title" style="left:135px;top:29px">Mining company<br>and lorem business</p>
  <p class="a copy" style="left:135px;top:46px;width:80px">Sed ut turpis a elit finibus elementum id luctus venenatis tellus at nisi dignissim.</p>
  <div class="a" style="left:135px;top:68px;width:80px;height:.5px;background:#ddd"></div>
  <div class="a icon" style="left:14px;top:93px;width:13px;height:13px"><svg viewBox="0 0 10 10"><path d="M1 5L5 1l4 4v4H1z" fill="none" stroke="#fff"/></svg></div>
  <p class="a label" style="left:32px;top:92px">House building</p><p class="a copy" style="left:32px;top:98px;width:38px">Nam sit amet libero at mi elementum.</p>
  <div class="a icon" style="left:83px;top:93px;width:13px;height:13px"><svg viewBox="0 0 10 10"><rect x="1" y="3" width="8" height="5" fill="none" stroke="#fff"/></svg></div>
  <p class="a label" style="left:101px;top:92px">Concrete surfaces</p><p class="a copy" style="left:101px;top:98px;width:38px">Duis tempus lectus in ultricies.</p>
  <div class="a icon" style="left:152px;top:93px;width:13px;height:13px"><svg viewBox="0 0 10 10"><path d="M2 8l6-6M2 2l6 6" stroke="#fff"/></svg></div>
  <p class="a label" style="left:170px;top:92px">Renovation</p><p class="a copy" style="left:170px;top:98px;width:44px">Sed convallis nunc eu nisl venenatis.</p>
</section>

<!-- 26 Latest projects -->
<section class="slide">
  <div class="a navy" style="left:0;top:0;width:94px;height:3px"></div>
  <p class="a title" style="left:15px;top:32px">Our latest projects</p>
  <p class="a copy" style="left:15px;top:43px;width:90px">Donec nibh nibh, sagittis vel purus ac lobortis eleifend dui nunc turpis erat blandit id nunc blandit.</p>
  <p class="a copy" style="left:15px;top:60px;width:90px">Etiam venenatis in lacus eu maximus proin id erat.</p>
  <div class="a" style="left:15px;top:78px;width:82px;height:.5px;background:#ddd"></div>
  <p class="a copy" style="left:15px;top:86px;width:90px">Aliquam at ornare mi consectetur convallis leo quis dolor sapien tempor nisi nunc semper.</p>
  <div class="a photo-truck" role="img" aria-label="Dump truck at a mining site" style="left:113px;top:13px;width:87px;height:50px"></div>
  <div class="a photo-pit" role="img" aria-label="Quarry terraces" style="left:113px;top:68px;width:40px;height:28px"></div>
  <div class="a photo-pit" role="img" aria-label="Mining area from above" style="left:159px;top:68px;width:41px;height:28px"></div>
  <div class="a gold" style="left:213px;top:0;width:13px;height:127px"></div>
</section>

<!-- 27 Project title navy -->
<section class="slide">
  <div class="a navy" style="left:0;top:0;width:71px;height:127px"></div>
  <p class="a title on-dark" style="left:15px;top:26px">Project title<br>goes here</p>
  <p class="a copy on-dark" style="left:15px;top:42px;width:48px">Mauris magna turpis interdum vel ac et sagittis auctor ipsum.</p>
  <p class="a copy on-dark" style="left:15px;top:58px;width:48px">Maecenas ac ultrices ipsum quis tincidunt lectus.</p>
  <div class="a" style="left:15px;top:72px;width:48px;height:.5px;background:#fff"></div>
  <p class="a copy on-dark" style="left:15px;top:80px;width:52px">Client &nbsp;&nbsp;&nbsp;Northfield Corporate<br>Budget &nbsp;$2 000 000.00<br>Date &nbsp;&nbsp;&nbsp;&nbsp;20 September 2017</p>
  <div class="a photo-digger" role="img" aria-label="Backhoe loader on a dirt site" style="left:86px;top:13px;width:57px;height:101px"></div>
  <div class="a photo-truck" role="img" aria-label="Dump truck near a quarry" style="left:149px;top:48px;width:65px;height:66px"></div>
</section>

<!-- 28 Project details -->
<section class="slide">
  <div class="a photo-dusk" role="img" aria-label="Excavators on a large construction site" style="left:0;top:0;width:226px;height:60px"></div>
  <p class="a title" style="left:15px;top:74px">Project title goes here</p>
  <p class="a copy" style="left:15px;top:86px;width:115px">Mauris magna turpis lobortis sed ut est et sagittis auctor ipsum donec tincidunt hendrerit faucibus lorem ipsum.</p>
  <p class="a copy" style="left:15px;top:103px;width:115px">Maecenas et ultricies tellus pharetra augue amet nulla est sed tristique.</p>
  <p class="a label" style="left:142px;top:78px">Project details</p>
  <p class="a copy" style="left:142px;top:95px;width:75px">Client &nbsp;&nbsp;Northfield Corporate<br>Budget &nbsp;$2 000 000.00<br>Date &nbsp;&nbsp;&nbsp;20 September 2017</p>
</section>

<!-- 29 Latest projects 1 -->
<section class="slide">
  <p class="a title" style="left:15px;top:15px">Our latest projects</p>
  <p class="a copy" style="left:15px;top:27px;width:98px">Sed convallis nunc eu nisl venenatis nec sagittis augue sagittis proin consectetur sagittis nec interdum.</p>
  <div class="a photo-pit" role="img" aria-label="Loader by a sand pile and drilling rig" style="left:120px;top:0;width:106px;height:55px"></div>
  <div class="a photo-worker" role="img" aria-label="Worker in hard hat flying a drone" style="left:14px;top:56px;width:92px;height:57px"></div>
  <p class="a label" style="left:120px;top:68px">Project title goes here 1</p>
  <p class="a copy" style="left:120px;top:75px;width:90px">Pellentesque a ipsum tempor orci mauris in turpis vitae odio tristique dignissim.</p>
  <p class="a copy" style="left:120px;top:92px;width:80px">Client &nbsp;&nbsp;Northfield Corporate<br>Budget &nbsp;$2 000 000.00<br>Date &nbsp;&nbsp;&nbsp;20 September 2017</p>
</section>

<!-- 30 Latest projects 2 -->
<section class="slide">
  <div class="a gold" style="left:0;top:0;width:226px;height:2px"></div>
  <div class="a photo-worker" role="img" aria-label="Drone remote control in hand" style="left:14px;top:25px;width:72px;height:34px"></div>
  <div class="a photo-pit" role="img" aria-label="Open-pit mine from above" style="left:14px;top:63px;width:72px;height:50px"></div>
  <p class="a label" style="left:110px;top:27px">Project title goes here 2</p>
  <p class="a copy" style="left:110px;top:34px;width:102px">Sed convallis nunc eu nisl venenatis nec sagittis augue sagittis proin consectetur sagittis nec interdum lorem ipsum.</p>
  <p class="a copy" style="left:110px;top:53px;width:102px">Luctus suscipit mauris mi pretium at ligula eleifend condimentum ut sem.</p>
  <p class="a copy" style="left:110px;top:70px;width:102px">Nulla sollicitudin eget elit malesuada tincidunt suspendisse sapien.</p>
  <p class="a copy" style="left:110px;top:92px;width:80px">Client &nbsp;&nbsp;Northfield Corporate<br>Budget &nbsp;$2 000 000.00<br>Date &nbsp;&nbsp;&nbsp;20 September 2017</p>
</section>

<!-- 31 Achievements -->
<section class="slide navy">
  <div class="a photo-city" role="img" aria-label="Loader in front of a city skyline" style="left:14px;top:0;width:92px;height:48px"></div>
  <p class="a title on-dark" style="left:122px;top:26px">Company achievements</p>
  <p class="a copy on-dark" style="left:122px;top:36px;width:90px">Sed convallis nunc eu nisl venenatis nec sagittis augue sagittis proin consectetur.</p>
  <div class="a dot" style="left:14px;top:64px;width:12px;height:12px;font-size:3px">70%</div>
  <p class="a label on-dark" style="left:35px;top:63px">The awesome title goes here</p><p class="a copy on-dark" style="left:35px;top:69px;width:64px">Nam sit amet libero at mi elementum vulputate non in gravida.</p>
  <div class="a dot" style="left:122px;top:64px;width:12px;height:12px;font-size:3px">72%</div>
  <p class="a label on-dark" style="left:141px;top:63px">Interior design title goes here</p><p class="a copy on-dark" style="left:141px;top:69px;width:72px">Nam sit amet libero at mi elementum vulputate non in gravida.</p>
  <div class="a dot" style="left:14px;top:92px;width:12px;height:12px;font-size:3px">69%</div>
  <p class="a label on-dark" style="left:35px;top:91px">Architectural title goes here</p><p class="a copy on-dark" style="left:35px;top:97px;width:64px">Nam sit amet libero at mi elementum vulputate non in gravida.</p>
  <div class="a dot" style="left:122px;top:92px;width:12px;height:12px;font-size:3px">65%</div>
  <p class="a label on-dark" style="left:141px;top:91px">Construction title goes here</p><p class="a copy on-dark" style="left:141px;top:97px;width:72px">Nam sit amet libero at mi elementum vulputate non in gravida.</p>
</section>

<!-- 32 Offices -->
<section class="slide">
  <p class="a title" style="left:15px;top:15px">Our offices<br>around the world</p>
  <p class="a copy" style="left:15px;top:34px;width:100px">Donec vel ipsum augue vitae viverra eros nunc bibendum vehicula ut lacinia morbi et magna.</p>
  <div class="a gold" role="img" aria-label="World map marking four office locations" style="left:15px;top:55px;width:110px;height:55px;border-radius:10px 18px 8px 14px;opacity:.85"></div>
  <p class="a label" style="left:140px;top:14px"><span class="num" style="font-size:5px">01.</span> New York, United States</p><p class="a copy" style="left:140px;top:21px;width:72px">Donec massa ante maximus condimentum tortor.</p>
  <p class="a label" style="left:140px;top:41px"><span class="num" style="font-size:5px">02.</span> Brasilia, Brazil</p><p class="a copy" style="left:140px;top:48px;width:72px">Donec massa ante maximus condimentum tortor.</p>
  <p class="a label" style="left:140px;top:68px"><span class="num" style="font-size:5px">03.</span> London, United Kingdom</p><p class="a copy" style="left:140px;top:75px;width:72px">Donec massa ante maximus condimentum tortor.</p>
  <p class="a label" style="left:140px;top:95px"><span class="num" style="font-size:5px">04.</span> Beijing, China</p><p class="a copy" style="left:140px;top:102px;width:72px">Donec massa ante maximus condimentum tortor.</p>
</section>

<!-- 33 Structures Congo -->
<section class="slide">
  <div class="a navy" style="left:0;top:0;width:120px;height:127px"></div>
  <p class="a title on-dark" style="left:15px;top:15px">Our structures<br>in Democratic Republic of Congo</p>
  <p class="a copy on-dark" style="left:15px;top:35px;width:95px">Fusce tincidunt nulla vel metus at blandit hac platea dictumst feugiat nisl vulputate nulla vivamus.</p>
  <p class="a label on-dark" style="left:15px;top:66px"><span class="num" style="font-size:5px">01.</span> London, United Kingdom</p>
  <p class="a copy on-dark" style="left:15px;top:73px;width:95px">Praesent tempor leo in commodo mattis quisque sed eros orci lorem.</p>
  <p class="a label on-dark" style="left:15px;top:92px"><span class="num" style="font-size:5px">02.</span> Liverpool, United Kingdom</p>
  <p class="a copy on-dark" style="left:15px;top:99px;width:95px">Suspendisse at malesuada turpis duis ut nisl vel dolor euismod.</p>
  <div class="a map-gold" role="img" aria-label="Map of the Republic of Congo with southern regions highlighted" style="left:132px;top:14px;width:78px;height:100px;border-radius:30px 8px 20px 6px"></div>
</section>

<!-- 34 Investment areas -->
<section class="slide">
  <p class="a title" style="left:15px;top:13px">The best investment<br>areas in Democratic<br>Republic of Congo</p>
  <p class="a copy" style="left:15px;top:40px;width:85px">Morbi tempus metus et rhoncus congue accumsan nulla faucibus ornare massa.</p>
  <div class="a" style="left:15px;top:61px;width:80px;height:3px;background:linear-gradient(90deg,#fbe4a8,#f2a900,#8a5d00)"></div>
  <p class="a copy" style="left:15px;top:66px;width:80px;word-spacing:6px">100 200 300 400 500 600</p>
  <p class="a copy" style="left:15px;top:78px;width:85px;color:var(--ink)">Nam aliquet elementum massa nec sollicitudin risus fringilla.</p>
  <p class="a copy" style="left:15px;top:92px;width:85px">Ut sed nunc duis porta sollicitudin id pellentesque mauris ac blandit tellus.</p>
  <div class="a navy" style="left:0;top:124px;width:94px;height:3px"></div>
  <div class="a map-gold" role="img" aria-label="Map of the Republic of Congo with investment areas shaded" style="left:126px;top:14px;width:86px;height:100px;border-radius:30px 8px 20px 6px"></div>
</section>

<!-- 35 Mining teams -->
<section class="slide">
  <div class="a navy" style="left:213px;top:0;width:13px;height:127px"></div>
  <div class="a map-gold" role="img" aria-label="Map of the Republic of Congo with team regions highlighted" style="left:14px;top:14px;width:86px;height:100px;border-radius:30px 8px 20px 6px"></div>
  <p class="a title" style="left:125px;top:14px">Mining teams in<br>Democratic Republic<br>of Congo</p>
  <p class="a copy" style="left:125px;top:40px;width:80px">Morbi tempus metus et rhoncus congue accumsan nulla faucibus.</p>
  <div class="a" style="left:125px;top:59px;width:52px;height:5px;background:repeating-linear-gradient(90deg,var(--navy) 0 3px,transparent 3px 4.6px)"></div><p class="a copy accent" style="left:198px;top:60px">98%</p>
  <div class="a" style="left:125px;top:73px;width:52px;height:5px;background:repeating-linear-gradient(90deg,#b98a1c 0 3px,transparent 3px 4.6px)"></div><p class="a copy accent" style="left:198px;top:74px">72%</p>
  <div class="a" style="left:125px;top:87px;width:52px;height:5px;background:repeating-linear-gradient(90deg,#d79b0e 0 3px,transparent 3px 4.6px)"></div><p class="a copy accent" style="left:198px;top:88px">63%</p>
  <div class="a" style="left:125px;top:101px;width:52px;height:5px;background:repeating-linear-gradient(90deg,var(--gold) 0 3px,transparent 3px 4.6px)"></div><p class="a copy accent" style="left:198px;top:102px">51%</p>
</section>

<!-- 36 Questions -->
<section class="slide navy">
  <div class="a photo-person" role="img" aria-label="Businessman in suit on the phone" style="left:14px;top:13px;width:92px;height:101px"></div>
  <div class="a" style="left:106px;top:59px;width:120px;height:68px;background:#fff"></div>
  <p class="a title on-dark" style="left:122px;top:18px">Questions?<br>Contact us now!</p>
  <p class="a copy on-dark" style="left:122px;top:36px;width:92px">Dictumst feugiat nisl vulputate nulla vivamus fringilla rhoncus pellentesque.</p>
  <p class="a label" style="left:122px;top:77px">New York, USA</p>
  <p class="a copy" style="left:122px;top:83px;width:44px">18 Crane Ave<br>NY 10001, United States<br>ny@varomel.com<br>+1 212 555 0100</p>
  <p class="a label" style="left:172px;top:77px">London, UK</p>
  <p class="a copy" style="left:172px;top:83px;width:44px">9 Mercer Rd<br>Bolton BL4, United Kingdom<br>uk@varomel.com<br>+44 1204 555 010</p>
</section>

<!-- 37 Contact -->
<section class="slide">
  <div class="a photo-city" role="img" aria-label="Wheel loader in front of a city skyline" style="left:0;top:0;width:226px;height:127px"></div>
  <div class="a" style="left:0;top:80px;width:114px;height:47px;background:#fff"></div>
  <div class="a brand" style="left:16px;top:104px"><i></i>VAROMEL</div>
  <div class="a navy" style="left:114px;top:14px;width:99px;height:100px"></div>
  <div class="a gold" style="left:114px;top:112px;width:99px;height:2px"></div>
  <p class="a title on-dark" style="left:128px;top:28px">Contact us</p>
  <p class="a copy on-dark" style="left:128px;top:39px;width:78px">Dictumst feugiat nisl vulputate nulla vivamus fringilla rhoncus pellentesque.</p>
  <div class="a icon" style="left:128px;top:56px;width:6px;height:6px"></div><p class="a copy on-dark" style="left:138px;top:56px">18 Crane Ave, New York<br>United States</p>
  <div class="a icon" style="left:128px;top:70px;width:6px;height:6px"></div><p class="a copy on-dark" style="left:138px;top:70px">contact@varomel.com<br>www.varomel.com</p>
  <div class="a icon" style="left:128px;top:84px;width:6px;height:6px"></div><p class="a copy on-dark" style="left:138px;top:84px">+1 212 555 0100<br>+1 212 555 0200</p>
</section>

<!-- 38 Office -->
<section class="slide">
  <div class="a gold" style="left:0;top:0;width:14px;height:127px"></div>
  <div class="a navy" style="left:14px;top:0;width:106px;height:127px"></div>
  <p class="a title on-dark" style="left:28px;top:32px">Our office</p>
  <p class="a copy on-dark" style="left:28px;top:42px;width:82px">Dictumst feugiat nisl vulputate nulla vivamus fringilla rhoncus pellentesque.</p>
  <div class="a icon" style="left:28px;top:60px;width:6px;height:6px"></div><p class="a copy on-dark" style="left:38px;top:60px">18 Crane Ave, New York<br>United States</p>
  <div class="a icon" style="left:28px;top:74px;width:6px;height:6px"></div><p class="a copy on-dark" style="left:38px;top:74px">contact@varomel.com<br>www.varomel.com</p>
  <div class="a icon" style="left:28px;top:88px;width:6px;height:6px"></div><p class="a copy on-dark" style="left:38px;top:88px">+1 212 555 0100<br>+1 212 555 0200</p>
  <div class="a photo-dark" role="img" aria-label="Rooftop water tower among city buildings" style="left:126px;top:14px;width:86px;height:100px"></div>
</section>

<!-- 39 Thanks dark -->
<section class="slide">
  <div class="a photo-dark" role="img" aria-label="Mining conveyor structure at dusk" style="left:0;top:0;width:226px;height:127px"></div>
  <div class="a gold" style="left:0;top:0;width:226px;height:12px"></div>
  <div class="a navy" style="left:14px;top:0;width:70px;height:40px"></div>
  <div class="a brand on-dark" style="left:33px;top:20px"><i></i>VAROMEL</div>
  <p class="a title on-dark" style="left:96px;top:38px">Thanks for watching</p>
  <div class="a gold" style="left:96px;top:47px;width:22px;height:1px"></div>
  <p class="a copy on-dark" style="left:96px;top:52px;width:92px">Aliquam ultricies mauris non leo maximus vehicula ut accumsan nisl tellus.</p>
  <div class="a icon" style="left:96px;top:68px;width:5px;height:5px"></div><p class="a copy on-dark" style="left:104px;top:68px">18 Crane Ave, New York, NY 10001</p>
  <div class="a icon" style="left:96px;top:76px;width:5px;height:5px"></div><p class="a copy on-dark" style="left:104px;top:76px">contact@varomel.com</p>
  <div class="a icon" style="left:96px;top:84px;width:5px;height:5px"></div><p class="a copy on-dark" style="left:104px;top:84px">+1 212 555 0100</p>
</section>

<!-- 40 Thank you -->
<section class="slide">
  <div class="a photo-dark" role="img" aria-label="Engineer in safety vest at a construction site" style="left:0;top:0;width:226px;height:127px"></div>
  <div class="a navy" style="left:217px;top:0;width:9px;height:127px"></div>
  <div class="a brand on-dark" style="left:15px;top:12px"><i></i>VAROMEL</div>
  <p class="a title on-dark xl" style="left:15px;top:27px;font-size:10px">Thank you<br>for watching</p>
  <div class="a gold" style="left:15px;top:55px;width:22px;height:1px"></div>
  <p class="a label on-dark" style="left:15px;top:78px">New York, USA</p>
  <p class="a copy on-dark" style="left:15px;top:84px;width:44px">18 Crane Ave<br>NY 10001, United States<br>ny@varomel.com<br>+1 212 555 0100</p>
  <p class="a label on-dark" style="left:63px;top:78px">London, UK</p>
  <p class="a copy on-dark" style="left:63px;top:84px;width:44px">9 Mercer Rd<br>Bolton BL4, UK<br>uk@varomel.com<br>+44 1204 555 010</p>
  <p class="a label on-dark" style="left:111px;top:78px">Warsaw, Poland</p>
  <p class="a copy on-dark" style="left:111px;top:84px;width:44px">Lipowa 14/26<br>00-377 Warsaw<br>pl@varomel.com<br>+48 22 555 010</p>
  <p class="a label on-dark" style="left:159px;top:78px">Kiev, Ukraine</p>
  <p class="a copy on-dark" style="left:159px;top:84px;width:44px">Sadova St 20<br>Kyiv, Ukraine<br>ua@varomel.com<br>+380 44 555 010</p>
</section>

</main>
</body>
</html>
```